Veterinary Pylon

My veterinary clinic is not clearly visible from the street and I want to place a Pylon next to my driveway. I want a modern, elegant straight Design, the Photo shows the sheduled place. One can see the clinic on our Homepage: www.lindbrook-pet-klinik.at
The last pictures are examples for pylones I like

Target Market(s)

the passing cars often miss my entry...I want to show where to turn left

Colors
3276b5
33a6d7
00a990

Requirements
Must have
• High value, simple elegance, size: 250cm (high) x 100cm (width)
Nice to have
• Our Logo, arrow(?)

A special Text is not necessary but this will be an option:

Biegen sie hier ab und wir biegen es wieder hin!
Should not have
• Too much Color, the colors I have chosen are the possible colors but it‘s not necessary to use them.

```html
<!DOCTYPE html>
<html lang="de">
<head>
<meta charset="utf-8">
<title>Lindbrook Pet Klinik – Pylon</title>
<link href="https://fonts.googleapis.com/css2?family=Fira+Sans:wght@400;500;700&display=swap" rel="stylesheet">
<style>
  :root {
    --brand-blue: #3276b5;
    --brand-cyan: #33a6d7;
    --deep-blue: #1f4f96;
    --frame: #7a7a7a;
    --panel: #ffffff;
    --page: #ffffff;
  }
  html, body {
    margin: 0;
    padding: 0;
    width: 1200px;
    height: 1121px;
    overflow: hidden;
    background: var(--page);
    font-family: "Fira Sans", Arial, sans-serif;
  }
  .pylon {
    position: absolute;
    left: 394px;
    top: 30px;
    width: 413px;
    height: 1062px;
    box-sizing: border-box;
    border: 3px solid var(--frame);
    border-radius: 3px;
    background: var(--panel);
    overflow: hidden;
  }
  .brand {
    position: absolute;
    top: 86px;
    left: 0;
    right: 0;
    display: flex;
    align-items: center;
    justify-content: center;
    gap: 14px;
  }
  .brand-dot {
    width: 34px;
    height: 34px;
    border-radius: 50%;
    background: var(--brand-cyan);
  }
  .brand-name {
    font-weight: 700;
    font-size: 30px;
    line-height: 1.1;
    color: var(--brand-blue);
  }
  .direction-band {
    position: absolute;
    top: 208px;
    left: 0;
    right: 0;
    height: 214px;
    background: var(--brand-blue);
  }
  .direction-text {
    position: absolute;
    left: 31px;
    top: 52px;
    margin: 0;
    color: #fff;
    font-weight: 500;
    font-size: 25px;
    line-height: 36px;
  }
  .direction-arrow {
    position: absolute;
    left: 313px;
    top: 56px;
    width: 84px;
    height: 84px;
  }
  .call-label {
    position: absolute;
    left: 31px;
    top: 449px;
    margin: 0;
    color: var(--brand-cyan);
    font-weight: 500;
    font-size: 24px;
  }
  .call-number {
    position: absolute;
    left: 31px;
    top: 487px;
    margin: 0;
    color: var(--deep-blue);
    font-weight: 700;
    font-size: 27px;
    letter-spacing: 0.5px;
  }
  .hours-heading {
    position: absolute;
    left: 0;
    top: 547px;
    width: 334px;
    height: 35px;
    box-sizing: border-box;
    padding-left: 31px;
    background: var(--brand-blue);
    border-radius: 0 12px 12px 0;
    color: #fff;
    font-weight: 700;
    font-size: 17px;
    line-height: 35px;
    letter-spacing: 0.5px;
  }
  .hours-list {
    position: absolute;
    left: 31px;
    top: 586px;
    margin: 0;
    font-size: 17px;
    line-height: 24px;
  }
  .hours-list dt {
    color: var(--brand-cyan);
    font-weight: 400;
  }
  .hours-list dd {
    margin: 0;
    color: var(--deep-blue);
    font-weight: 700;
  }
</style>
</head>
<body>
  <main class="pylon">
    <header class="brand">
      <span class="brand-dot" aria-hidden="true"></span>
      <span class="brand-name">Lindbrook Pet Klinik</span>
    </header>

    <section class="direction-band">
      <p class="direction-text">Biegen Sie Hier<br>Ab Und Wir Biegen<br>Es Wieder Hin!</p>
      <svg class="direction-arrow" viewBox="0 0 84 84" aria-label="Links abbiegen" role="img">
        <circle cx="42" cy="42" r="42" fill="#fff"/>
        <path d="M18 42 L36 27 L36 37 L64 37 L64 47 L36 47 L36 57 Z" fill="var(--brand-blue)"/>
      </svg>
    </section>

    <p class="call-label">Rufen Sie uns an:</p>
    <p class="call-number">+43 3198 40217</p>

    <div class="hours-heading">UNSERE ORDINATIONSZEITEN:</div>
    <dl class="hours-list">
      <dt>Montag bis Freitag</dt>
      <dd>8:00-12:00 / 14:00-19:00</dd>
      <dt>Samstag</dt>
      <dd>8:00-12:00 / 17:00-18:00</dd>
      <dt>Sonntag</dt>
      <dd>10:00-11:00 / 17:00-18:00</dd>
    </dl>
  </main>
</body>
</html>
```